Business card design for online Mandarin Learning School

We need a business card design for our online language learning school called "Maple Bridge Online for Mandarin Learning". Our existing website is https://www.maplebridgeonline.com
We have our logo already. We would like to see our business card design that can make our online teaching services to be innovative, young, energetic and fun to learn. Prefer to have a certain level of color matching with our website. Apart from "Maple Bridge Online", need to specifically state "for Mandarin Learning" as well on the business card.

```html
<!DOCTYPE html>
<html lang="en">
<head>
<meta charset="utf-8">
<title>Maple Bridge Online — Business Card</title>
<link href="https://fonts.googleapis.com/css2?family=Cinzel:wght@400;500;600&family=Lato:wght@400&display=swap" rel="stylesheet">
<style>
  :root {
    --backdrop: #2e2e2e;
    --card-white: #ffffff;
    --teal: #12a9b5;
    --teal-light: #7fd3da;
    --grey: #888888;
    --name-grey: #7a7a7a;
    --text-grey: #555555;
    --rule: #cfcfcf;
    --coral: #e2615d;
  }
  * { margin: 0; padding: 0; box-sizing: border-box; }
  html, body {
    width: 1200px; height: 1200px; overflow: hidden;
    background: var(--backdrop);
  }
  .canvas { position: relative; width: 1200px; height: 1200px; }
  .card {
    position: absolute; top: 310px; height: 594px; overflow: hidden;
    box-shadow: 0 4px 10px rgba(0,0,0,0.45);
  }
  .card--front { left: 234px; width: 364px; background: var(--card-white); }
  .card--back { left: 627px; width: 369px; background: var(--grey); }

  .brand-dot {
    position: absolute; left: 170px; top: 178px; width: 24px; height: 24px;
    border-radius: 50%; background: var(--coral);
  }
  .brand-name {
    position: absolute; left: 0; top: 215px; width: 100%; text-align: center;
    font-family: "Cinzel", serif; font-weight: 400; font-size: 36px;
    color: var(--teal); letter-spacing: 0.5px;
  }
  .person-name {
    position: absolute; top: 331px; width: 100%; text-align: center;
    font-family: "Cinzel", serif; font-weight: 500; font-size: 26px; color: var(--teal);
  }
  .person-name .surname { color: var(--name-grey); }
  .person-role {
    position: absolute; top: 360px; width: 100%; text-align: center;
    font-family: "Lato", sans-serif; font-size: 17px; color: var(--text-grey);
  }
  .icon-row {
    position: absolute; top: 396px; left: 87px; width: 190px; height: 24px;
    display: flex; align-items: center; justify-content: center; gap: 3px;
  }
  .icon-row .line { flex: 1; height: 1px; background: var(--grey); }
  .icon-row svg { width: 24px; height: 24px; }
  .contact {
    position: absolute; width: 100%; text-align: center;
    font-family: "Lato", sans-serif; font-size: 17px; color: var(--text-grey);
    line-height: 22px;
  }
  .contact--lines { top: 431px; }
  .contact--address { top: 517px; }
  .divider {
    position: absolute; top: 506px; left: 88px; width: 196px; height: 1px; background: var(--rule);
  }

  .back-field {
    position: absolute; top: 0; left: 0; width: 100%; height: 430px; background: var(--teal);
  }
  .back-artwork {
    position: absolute; left: 28px; top: 145px; width: 312px; height: 310px;
    border-radius: 50% 50% 46% 46%;
    background: radial-gradient(ellipse at 50% 60%, rgba(255,255,255,0.55) 0%, rgba(255,255,255,0.28) 45%, rgba(127,211,218,0) 72%);
  }
  .back-title {
    position: absolute; top: 489px; width: 100%; text-align: center;
    font-family: "Cinzel", serif; font-weight: 600; font-size: 29px; color: #ffffff;
  }
  .back-tagline {
    position: absolute; top: 523px; width: 100%; text-align: center;
    font-family: "Lato", sans-serif; font-size: 17px; color: #ffffff;
  }
</style>
</head>
<body>
<main class="canvas">
  <section class="card card--front">
    <span class="brand-dot"></span>
    <div class="brand-name">MAPLE BRIDGE</div>
    <div class="person-name">DANIEL <span class="surname">HAYES</span></div>
    <div class="person-role">Managing Director</div>
    <div class="icon-row">
      <span class="line"></span>
      <svg viewBox="0 0 24 24" aria-label="Phone"><circle cx="12" cy="12" r="12" fill="var(--teal)"/><path d="M7 9c0-1 1-2 5-2s5 1 5 2v1h-3V9h-4v1H7zM8 11h8l1 6H7z" fill="#fff"/></svg>
      <svg viewBox="0 0 24 24" aria-label="Email"><circle cx="12" cy="12" r="12" fill="var(--teal)"/><rect x="6.5" y="8" width="11" height="8" fill="#fff"/><path d="M6.5 8l5.5 4.5L17.5 8" fill="none" stroke="var(--teal)" stroke-width="1.2"/></svg>
      <svg viewBox="0 0 24 24" aria-label="Website"><circle cx="12" cy="12" r="12" fill="var(--teal)"/><circle cx="12" cy="12" r="5.5" fill="none" stroke="#fff" stroke-width="1.5"/><path d="M6.5 12h11M12 6.5c-2.5 3-2.5 8 0 11M12 6.5c2.5 3 2.5 8 0 11" fill="none" stroke="#fff" stroke-width="1.2"/></svg>
      <span class="line"></span>
    </div>
    <div class="contact contact--lines">044-987 654 321<br>hello@maplebridgeonline.com<br>www.maplebridgeonline.com</div>
    <span class="divider"></span>
    <div class="contact contact--address">218, Harbour Lane,<br>30517, Sample Country</div>
  </section>

  <section class="card card--back">
    <div class="back-field"></div>
    <div class="back-artwork" role="img" aria-label="Large brand artwork: joyful figures rising from an open book, white on teal"></div>
    <div class="back-title">MAPLE BRIDGE</div>
    <div class="back-tagline">Online for Mandarin Learning</div>
  </section>
</main>
</body>
</html>
```